Business Card

We are looking to re-create our business card. Attached is the company logo. we would like it to be back and front. for example one side with the persons information and the other side with the company logo. Be as creative as you would like but also keep in mind, we are a Health Insurance company and we need to look professional as well.
Industry/Entity Type
Business

```html
<!DOCTYPE html>
<html lang="en">
<head>
<meta charset="utf-8">
<title>Northvale Care Partners – Business Card</title>
<link href="https://fonts.googleapis.com/css2?family=Open+Sans:wght@400;600&display=swap" rel="stylesheet">
<style>
  :root {
    --backdrop: #d6d8da;
    --card: #f7f7f7;
    --brand-blue: #1a93d1;
    --brand-grey: #8a8c8e;
    --text-grey: #5d5f61;
    --rule: #b9bbbd;
  }
  * { box-sizing: border-box; margin: 0; padding: 0; }
  html, body {
    width: 1200px; height: 900px; overflow: hidden;
    background: var(--backdrop);
    font-family: "Open Sans", Arial, sans-serif;
  }
  .sheet {
    width: 1200px; height: 900px;
    display: flex; flex-direction: column;
    align-items: center; justify-content: center; gap: 44px;
  }
  .card {
    position: relative;
    width: 660px; height: 378px;
    background: var(--card);
    border-radius: 34px;
    box-shadow: 0 2px 6px rgba(0,0,0,0.12);
  }

  /* Front: brand side */
  .card-front .brand {
    position: absolute; left: 86px; top: 150px;
    display: flex; align-items: center; gap: 14px;
  }
  .brand-square {
    width: 30px; height: 30px; background: var(--brand-blue); border-radius: 4px;
  }
  .brand-name {
    font-size: 38px; font-weight: 600; color: var(--brand-blue); letter-spacing: -0.3px;
  }
  .card-front .website {
    position: absolute; left: 130px; top: 212px;
    font-size: 15px; color: var(--brand-blue);
  }

  /* Back: contact side */
  .card-back .header {
    position: absolute; left: 56px; top: 64px;
    display: flex; align-items: center; gap: 18px;
  }
  .header .brand-square { width: 18px; height: 18px; border-radius: 3px; }
  .header .initials { font-size: 28px; font-weight: 600; color: var(--brand-grey); }
  .header .divider { width: 1px; height: 58px; background: var(--rule); }
  .header .company { font-size: 22px; font-weight: 600; color: var(--brand-blue); }

  .person {
    position: absolute; left: 56px; top: 196px;
    display: flex; align-items: baseline; gap: 8px;
  }
  .person-name { font-size: 26px; color: var(--brand-blue); }
  .person-role { font-size: 13px; color: var(--text-grey); }

  .address {
    position: absolute; left: 56px; top: 250px;
    font-size: 13px; line-height: 1.6; color: var(--text-grey);
    font-style: normal;
  }
  .contact-rule {
    position: absolute; left: 330px; top: 200px;
    width: 1px; height: 118px; background: var(--rule);
  }
  .contacts {
    position: absolute; left: 352px; top: 204px;
    list-style: none; font-size: 13px; line-height: 1.6; color: var(--text-grey);
  }
  .contacts .label { color: var(--brand-blue); }
</style>
</head>
<body>
  <main class="sheet">
    <section class="card card-front" aria-label="Card front">
      <div class="brand">
        <span class="brand-square"></span>
        <span class="brand-name">Northvale Care Partners</span>
      </div>
      <p class="website">www.northvalecare.com</p>
    </section>

    <section class="card card-back" aria-label="Card back">
      <div class="header">
        <span class="brand-square"></span>
        <span class="initials">NCP</span>
        <span class="divider"></span>
        <span class="company">Northvale Care Partners</span>
      </div>

      <div class="person">
        <span class="person-name">Maya Ellison,</span>
        <span class="person-role">Managed Services</span>
      </div>

      <address class="address">
        Northvale Care Partners Pty Ltd<br>
        Level 4, 88 Harbour Lane<br>
        Sydney, NSW 2000 Australia
      </address>

      <span class="contact-rule"></span>

      <ul class="contacts">
        <li><span class="label">tel:</span> 1300 555 019</li>
        <li><span class="label">fax:</span> 61 2 5550 0191</li>
        <li><span class="label">email:</span> hello@northvalecare.com</li>
      </ul>
    </section>
  </main>
</body>
</html>
```